Harvest Ledger Group
Business Cards, Envelopes and Letterhead
Project: Harvest Ledger Group
Harvest Ledger Group -
Creative Brief
Bright & Fun-filled
Marcus T. Halvorsen
President
47 Brookmere Loop West, Suite B318 Englewood, CO 80214
mh@kt-assetpartners.com
www.kt-assetpartners.com

```html
<!DOCTYPE html>
<html lang="en">
<head>
<meta charset="utf-8">
<title>Harvest Ledger Group – Business Card</title>
<link href="https://fonts.googleapis.com/css2?family=Arimo:ital,wght@0,400;0,700;1,700&family=Tinos:wght@400;700&display=swap" rel="stylesheet">
<style>
  :root {
    --page-bg: #e9e6e2;
    --card-white: #ffffff;
    --brand-blue: #2b7cc4;
    --brand-blue-deep: #1f68ad;
    --text-white: #ffffff;
    --ink-dark: #1c1c1c;
    --divider: #d6d6d6;
  }
  * { margin: 0; padding: 0; box-sizing: border-box; }
  html, body {
    width: 1200px; height: 852px; overflow: hidden;
    background: var(--page-bg);
  }
  .canvas {
    position: relative; width: 1200px; height: 852px;
  }
  .business-card {
    position: absolute; left: 100px; top: 140px;
    width: 1000px; height: 572px;
    border-radius: 34px; overflow: hidden;
    display: flex;
    background: var(--card-white);
    box-shadow: 0 10px 30px rgba(0,0,0,.18);
  }
  .brand-side {
    width: 470px; height: 100%;
    display: flex; align-items: center; justify-content: center;
    background: var(--card-white);
    border-right: 3px solid var(--divider);
  }
  .brand-lockup {
    display: flex; align-items: center; gap: 18px;
  }
  .brand-square {
    width: 54px; height: 54px; background: var(--brand-blue);
  }
  .brand-name {
    font-family: "Tinos", serif; font-weight: 700;
    font-size: 34px; line-height: 1.05; color: var(--ink-dark);
    letter-spacing: .5px; text-transform: uppercase;
  }
  .contact-side {
    flex: 1; height: 100%;
    background: linear-gradient(180deg, var(--brand-blue) 0%, var(--brand-blue-deep) 100%);
    border-left: 6px solid var(--card-white);
    outline: 3px solid var(--brand-blue);
    color: var(--text-white);
    padding: 44px 40px 0 48px;
  }
  .person-name {
    font-family: "Arimo", sans-serif; font-weight: 700;
    font-size: 34px; font-style: italic;
  }
  .person-title {
    font-family: "Arimo", sans-serif; font-weight: 700; font-style: italic;
    font-size: 22px; margin-top: 8px;
  }
  .address {
    font-family: "Tinos", serif; font-size: 23px; line-height: 1.35;
    margin-top: 78px; width: 360px;
  }
  .contact-list {
    list-style: none; margin-top: 40px;
    font-family: "Tinos", serif; font-size: 23px;
  }
  .contact-list li {
    display: flex; align-items: center; gap: 14px; height: 33px;
  }
  .contact-icon { width: 20px; height: 20px; flex: none; }
</style>
</head>
<body>
<div class="canvas">
  <section class="business-card">
    <div class="brand-side">
      <div class="brand-lockup">
        <div class="brand-square"></div>
        <div class="brand-name">Harvest Ledger<br>Group</div>
      </div>
    </div>
    <div class="contact-side">
      <h1 class="person-name">Marcus T. Halvorsen</h1>
      <p class="person-title">President</p>
      <p class="address">47 Brookmere Loop West,<br>Suite B318<br>Englewood, CO 80214</p>
      <ul class="contact-list">
        <li>
          <svg class="contact-icon" viewBox="0 0 20 20"><path d="M5 2c1 0 2 3 2 4s-2 1-1 3 3 4 5 5 2-1 3-1 4 1 4 2-2 3-3 3C8 18 2 12 2 5c0-1 2-3 3-3z" fill="#fff"/></svg>
          <span>(303) 555-0142</span>
        </li>
        <li>
          <svg class="contact-icon" viewBox="0 0 20 20"><rect x="5" y="1" width="10" height="18" rx="2" fill="#fff"/><rect x="7" y="4" width="6" height="9" fill="#2b7cc4"/></svg>
          <span>(303) 555-0187</span>
        </li>
        <li>
          <svg class="contact-icon" viewBox="0 0 20 20"><rect x="2" y="8" width="16" height="10" rx="2" fill="#fff"/><rect x="5" y="2" width="10" height="7" fill="#fff"/><rect x="6" y="11" width="8" height="2" fill="#2b7cc4"/></svg>
          <span>888-555-0163</span>
        </li>
        <li>
          <svg class="contact-icon" viewBox="0 0 20 20"><circle cx="10" cy="10" r="9" fill="#fff"/><text x="10" y="14.5" font-family="Arimo, sans-serif" font-size="13" font-weight="700" fill="#2b7cc4" text-anchor="middle">@</text></svg>
          <span>mh@kt-assetpartners.com</span>
        </li>
        <li>
          <svg class="contact-icon" viewBox="0 0 20 20"><circle cx="10" cy="10" r="8.5" fill="none" stroke="#fff" stroke-width="2"/><ellipse cx="10" cy="10" rx="3.5" ry="8.5" fill="none" stroke="#fff" stroke-width="1.5"/><line x1="2" y1="10" x2="18" y2="10" stroke="#fff" stroke-width="1.5"/></svg>
          <span>www.kt-assetpartners.com</span>
        </li>
      </ul>
    </div>
  </section>
</div>
</body>
</html>
```